Looking for a cool, modern Cannabis Jar Label

I want you to come up with a better, modern look for a label.

I need it sized to 4” x 3” - I plan to print directly to label printer.

I want you to use Photoshop and deliver me a layered PSD file that I can edit and modify the information as needed..

The label information will need to include places for:
(1) Strain Name - most important part of label - larger font size than rest - example Marlow Frost, KTV #7, Copperleaf Haze
(2) Pricing - for Gram, 1/8, 1/4, 1/2. and Ounce
(3) Strain Designation (Hybrid, Indica or Sativa) - maybe color coded, different color for Indica v. Sativa, just an idea
(4) THC and CBD percentages - for example 23% THC and 0.05% CBD
(5) Farm name - a place where we can add the name/logo of the business that produced the product. example - Bramwell Farms

I have attached a simple mockup showing the information.

I have also attached a few samples of labels we like to give you an idea of the look and feel we are going for.

I am wanting a very clean, modern, classy, readable look.The font will use is Gotham Font.

HI Everyone! Thank you for all of your designs. I am requesting an extension because I need more time to give adequate feedback to the designers. Thank you for your participation and all of your efforts! I will be making a decision soon!

• Gotham Font

Designer to choose colors to be used in the design.

• Thank you for your designs. I am sorry i have been slow in providing feedback, things have been really busy around here!
• I wanted to give some group general feedback. After reviewing all of the designs, there is a common theme among all of the designs that I would like to see changed.
• I would like to see the per gram pricing more prominent on the label. This is what most people are looking for when they are purchasing the product. So I would like to see this stand out from the other pricing tiers. As I think about it, they don't all need to be grouped together in a line. You could have the Per Gram pricing front and center some where and then the other pricing tiers grouped together somewhere else on the label.
• This is the order of importance of items on the label. Items at the the top of the list should be bigger than those below it.
• 1. Strain name
• 2. Pricing - being per gram the most important of all prices
• 3. THC/CBD percentages
• 4. Strain Type (indica, sativa, hybrid)
• 5. Farm name/logo
• When laying out these labels, they will be going on rounded jars and they will be on display. Think of jars with fancy labels in a candy store. They need to be eye catchy, appealing, but easy read.
• Thank you for all of your hard work, everyone is doing a great job.
• Best,
• Nadia

```html
<!DOCTYPE html>
<html lang="en">
<head>
<meta charset="UTF-8">
<title>Strain Jar Label</title>
<link href="https://fonts.googleapis.com/css2?family=Montserrat:wght@400;500;700&display=swap" rel="stylesheet">
<style>
  :root {
    --forest: #168b45;
    --lime: #9dc93b;
    --pale: #c7df8f;
    --ink: #2b4724;
    --tier-label: #a8d14a;
  }
  * { margin: 0; padding: 0; box-sizing: border-box; }
  html, body { width: 1200px; height: 900px; overflow: hidden; background: #ffffff; }
  .label {
    position: relative;
    width: 1200px;
    height: 900px;
    overflow: hidden;
    font-family: "Montserrat", Arial, sans-serif;
    color: var(--ink);
    background: var(--lime);
  }
  .pricing-band {
    position: absolute; left: 0; top: 0; width: 1200px; height: 375px;
    background: var(--forest);
  }
  .farm-panel {
    position: absolute; left: 808px; top: 375px; width: 392px; height: 525px;
    background: var(--pale);
  }
  .strain-disc {
    position: absolute; left: -420px; top: -10px; width: 915px; height: 915px;
  }
  .strain-name {
    position: absolute; left: 62px; top: 318px;
    font-weight: 700; font-size: 80px; line-height: 96px; letter-spacing: 0.5px;
    text-transform: uppercase;
  }
  .price-tiers {
    position: absolute; left: 459px; top: 134px;
    display: flex; gap: 8px; list-style: none;
  }
  .tier { width: 136px; display: flex; flex-direction: column; align-items: center; }
  .tier:nth-child(2) { margin-right: 1px; }
  .tier-price {
    width: 136px; height: 136px; border-radius: 50%;
    background: var(--pale);
    display: flex; align-items: center; justify-content: center;
    font-weight: 700; font-size: 50px; letter-spacing: -1px;
  }
  .tier-price sup { font-size: 27px; position: relative; top: -9px; margin-right: 1px; vertical-align: baseline; }
  .tier-unit {
    margin-top: 14px;
    font-weight: 500; font-size: 25px; color: var(--tier-label);
    white-space: nowrap;
  }
  .strain-type {
    position: absolute; right: 435px; top: 466px;
    font-weight: 500; font-size: 52px; text-decoration: underline;
    text-decoration-thickness: 3px; text-underline-offset: 10px;
  }
  .potency {
    position: absolute; right: 430px; top: 648px; text-align: right;
    font-weight: 700; font-size: 60px; line-height: 90px;
  }
  .farm-name {
    position: absolute; left: 808px; top: 520px; width: 400px; text-align: center;
    font-weight: 400; font-size: 41px; line-height: 54px;
  }
</style>
</head>
<body>
<main class="label">
  <div class="pricing-band"></div>
  <div class="farm-panel"></div>

  <svg class="strain-disc" viewBox="0 0 915 915" role="img" aria-label="Soft watercolour leaf artwork">
    <defs>
      <radialGradient id="disc-tone" cx="0.35" cy="0.5" r="0.6">
        <stop offset="0" stop-color="#a9d167"/>
        <stop offset="0.6" stop-color="#bcdc82"/>
        <stop offset="1" stop-color="#c7df8f"/>
      </radialGradient>
    </defs>
    <circle cx="457.5" cy="457.5" r="457.5" fill="url(#disc-tone)"/>
  </svg>

  <h1 class="strain-name">Cedar<br>Creek<br>Chill</h1>

  <ul class="price-tiers">
    <li class="tier"><span class="tier-price"><sup>$</sup>10</span><span class="tier-unit">GRAM</span></li>
    <li class="tier"><span class="tier-price"><sup>$</sup>35</span><span class="tier-unit">1/8 OZ</span></li>
    <li class="tier"><span class="tier-price"><sup>$</sup>70</span><span class="tier-unit">1/4 OZ</span></li>
    <li class="tier"><span class="tier-price"><sup>$</sup>140</span><span class="tier-unit">1/2 OZ</span></li>
    <li class="tier"><span class="tier-price"><sup>$</sup>280</span><span class="tier-unit">OUNCE</span></li>
  </ul>

  <p class="strain-type">INDICIA</p>
  <p class="potency">28% THC<br>2% CBD</p>

  <p class="farm-name">FARM<br>LOGO<br>GOES<br>HERE</p>
</main>
</body>
</html>
```